Simple "top list" webpage (LiftYourBand.net)

Project Overview
The goal of the project is to make a webpage that shows a « top list » of artists which are currently raising funds on crowdfunding websites such as tunepledge, fansbackrecords, …
Visitors and artist’s producers will be able to vote for theirs artists
by 2 possibilities :
- 1 vote each day
- Buy a pack of a dozen vote for a limited amount of time
The more an artist has votes, the more he must be visible on the list to attract others producers.
Deliverables Required :
We need 2 types of deliverables for this project, to get full
webdesign package (no database backend, scripting, etc, ...) :
- A Logo (typography and/or image):
o 1 Image with logo + website name together
o 1 Image with image only (if it is chosen to make a
image+text logo…)
- A website design
o 1 html page with the general layout of the front page with the artist list
o Collection of images included in the design
Technical Requirements :
- No flash
- W3C stantards compliant
Audience
The audience profile is very heterogeneous, however :
- Music fans (style can be anything)
- Artists supporters
- Artist funders
- Talents anticipers
Tone
The global design should be modern and simple.
A typical visit will last no more than 1 minute, therefore the design shouldn’t distract too much the visitor. He must get straight to the
important information : the artist list.
Details :
The page should present a list of approximatively 15 artists (with
potential of other pages to get to the next ones)
Each Artist area should present the following informations
Artist Photo
Artist name
Fund raised (and maybe % of completion of fund raising)
Number of producers
Crowdfunding Platform
Number of votes
Tendency of votes (climbing, flat, down)
Updates
Reason: Period extended by 7 days in order to get the opportunity to get feedbacks and other contributions.
Reason: Hi All,
Thanks for all your quality submissions. As we are getting more designs, I extend deadlines in order to provide more feedback on submission.
Thanks again a lot.
Gerard

```html
<!DOCTYPE html>
<html lang="en">
<head>
<meta charset="utf-8">
<title>LiftYourBand.net – Top Artists</title>
<link rel="stylesheet" href="https://fonts.googleapis.com/css2?family=Arimo:wght@400;700&family=Roboto+Condensed:wght@400;700&family=Anton&family=Courier+Prime&display=swap">
<style>
:root{
  --page-bg:#f2f2f2;
  --side-bg:#1e1e1e;
  --side-panel:#2c2c2c;
  --ink-light:#ffffff;
  --ink-muted:#8c8c8c;
  --ink-dark:#111111;
  --pink:#ff7d87;
  --lime:#cfdc8a;
  --lime-dark:#b7c86a;
  --row-top:#ffffff;
  --row-bottom:#e3e3e3;
  --row-line:#2a2a2a;
  --rank:#8d8d8d;
  --up:#6c9a1c;
  --down:#c81d1d;
}
*{box-sizing:border-box;margin:0;padding:0}
html,body{width:1200px;height:1079px;overflow:hidden;background:var(--page-bg)}
body{font-family:Arimo,Arial,sans-serif}
.stage{position:relative;width:1152px;height:1034px;transform:scale(1.0417,1.0435);transform-origin:0 0}
.page{position:absolute;left:95px;top:0;width:960px;height:1034px;background:var(--side-bg);box-shadow:0 0 14px rgba(0,0,0,.25)}

/* sidebar */
.sidebar{position:absolute;left:0;top:0;width:329px;height:1034px;background:var(--side-bg);border-right:1px solid #000}
.brand{position:absolute;left:23px;top:22px;display:flex;align-items:center;gap:10px}
.brand-mark{width:26px;height:26px;background:var(--pink);border-radius:4px}
.brand-name{font-family:Anton,sans-serif;font-size:34px;color:var(--ink-light);letter-spacing:.5px;line-height:1}
.headline{position:absolute;left:22px;top:98px;font-family:"Roboto Condensed",sans-serif;font-weight:700;font-size:35px;line-height:36px;color:var(--ink-light);letter-spacing:-.5px}
.like-row{position:absolute;left:20px;top:187px;display:flex;align-items:center;gap:8px;font-size:11px;color:var(--ink-light);font-weight:700}
.like-btn{background:#eceef5;border:1px solid #cad4e7;border-radius:2px;color:#3b5998;font-size:11px;font-weight:700;padding:4px 7px}
.like-dot{width:11px;height:11px;background:#5d77ab;border-radius:2px}
.intro{position:absolute;left:19px;top:222px;width:290px;font-size:12.4px;line-height:17px;color:var(--ink-light)}
.intro p+p{margin-top:17px}
.buy-votes{position:absolute;left:19px;top:419px;font-size:21px;color:var(--lime)}
.member-box{position:absolute;left:11px;top:466px;width:306px;height:184px;background:var(--side-panel);border-radius:6px}
.signup-btn{position:absolute;left:7px;top:10px;width:289px;height:45px;border-radius:4px;background:linear-gradient(#ff9aa1,#ff6f7a);color:#fff;font-size:21px;font-weight:700;display:flex;align-items:center;justify-content:center;letter-spacing:-.5px;text-shadow:0 1px 1px rgba(0,0,0,.2)}
.signin-label{position:absolute;left:9px;top:72px;font-size:15px;color:var(--ink-light)}
.field{position:absolute;top:99px;width:119px;height:30px;background:#fff;border-radius:2px;font-size:13px;color:#222;padding:8px 10px}
.field.email{left:7px}
.field.password{left:134px}
.ok-btn{position:absolute;left:260px;top:99px;width:36px;height:30px;border-radius:5px;background:linear-gradient(#8a8a8a,#5a5a5a);color:#fff;font-size:12px;font-weight:700;display:flex;align-items:center;justify-content:center}
.forgot{position:absolute;left:8px;top:153px;font-size:12px;font-weight:700;color:var(--lime);text-decoration:underline}
.connect-btn{position:absolute;left:206px;top:149px;width:90px;height:21px;background:#3c5a97;border:1px solid #6d84b4;color:#fff;font-size:12px;font-weight:700;display:flex;align-items:center;justify-content:center;gap:6px}
.connect-btn .sq{width:9px;height:9px;background:#fff}
.follow{position:absolute;left:18px;top:670px;display:flex;align-items:center;gap:14px}
.follow-label{font-size:15px;font-weight:700;color:#ddd}
.follow-group{display:flex;width:197px;height:39px;border:1px solid #555;border-radius:5px;background:linear-gradient(#2d2d2d,#1a1a1a);overflow:hidden}
.follow-group a{flex:1;display:flex;align-items:center;justify-content:center;gap:6px;font-size:11.5px;font-weight:700;color:#ddd;text-decoration:none}
.follow-group a+a{border-left:1px solid #555}
.follow-group .dot{width:9px;height:9px;border-radius:50%;background:#bbb}
.promo{position:absolute;left:19px;top:726px;width:300px;height:250px;overflow:hidden;background:radial-gradient(circle at 120px 145px,#b7c255 0,#2d7a6a 22%,#0f2c2a 48%,#050505 75%)}
.promo-band{position:absolute;left:2px;top:4px;height:180px;writing-mode:vertical-rl;transform:rotate(180deg);text-align:left;font-family:"Roboto Condensed",sans-serif;font-weight:400;font-size:34px;line-height:40px;color:#fff;letter-spacing:3px;white-space:nowrap}
.promo-title{position:absolute;right:10px;top:6px;font-family:"Courier Prime",monospace;font-size:19px;color:#fff;white-space:nowrap}
.promo-sub{position:absolute;right:14px;top:32px;font-family:"Courier Prime",monospace;font-size:16px;color:#ccc;white-space:nowrap}
.promo-cta{position:absolute;right:12px;bottom:4px;font-size:16px;color:#fff}
.copyright{position:absolute;left:20px;top:1002px;font-size:12.5px;color:#aaa}

/* main list */
.main{position:absolute;left:330px;top:0;width:630px;height:1034px}
.main-head{height:108px;background:linear-gradient(#3a3a3a,#232323);position:relative}
.main-title{position:absolute;left:18px;top:18px;font-size:30px;font-weight:700;color:var(--ink-muted);letter-spacing:-.5px}
.pager{position:absolute;left:20px;display:flex;align-items:center;font-size:12.5px;font-weight:700;color:#fff}
.pager .label{font-size:16px;color:var(--ink-muted);margin-right:11px}
.pager a{color:#fff;text-decoration:none;padding:4px 11px;border-radius:3px}
.pager a.current{background:var(--pink)}
.main-head .pager{top:74px}
.artist-list{list-style:none}
.artist{position:relative;height:88px;background:linear-gradient(var(--row-top),var(--row-bottom));border-bottom:1px solid var(--row-line)}
.rank{position:absolute;left:0;width:75px;top:26px;text-align:center;font-size:33px;font-weight:700;color:var(--rank)}
.photo{position:absolute;left:78px;top:6px;width:77px;height:77px}
.name{position:absolute;left:168px;top:12px;font-size:18.5px;font-weight:700;color:var(--ink-dark);letter-spacing:-.3px}
.link{position:absolute;left:167px;top:62px;font-size:11.5px;font-weight:700;color:#222}
.funds{position:absolute;right:14px;top:61px;font-size:12.5px;font-weight:700;color:#111}
.votes{position:absolute;left:453px;top:12px;width:84px;height:30px;background:linear-gradient(#f6f6f6,#d2d2d2);clip-path:polygon(0 0,92% 0,100% 50%,92% 100%,0 100%);display:flex;align-items:center;padding-left:8px;gap:8px;font-size:18px;font-weight:700;color:#111}
.votes::before{content:"";width:0;height:0;border-left:5px solid transparent;border-right:5px solid transparent}
.votes.up::before{border-bottom:7px solid var(--up)}
.votes.down::before{border-top:7px solid var(--down)}
.vote-btn{position:absolute;left:547px;top:12px;width:65px;height:31px;border-radius:3px;background:linear-gradient(#d9e49c,var(--lime-dark));font-size:14px;font-weight:700;color:#222;display:flex;align-items:center;justify-content:center}
.main-foot{height:46px;background:linear-gradient(#2e2e2e,#1e1e1e);position:relative}
.main-foot .pager{top:14px;left:18px}

.ph-a{background:linear-gradient(135deg,#e8e2cf,#7b6a4a 60%,#2e2618)}
.ph-b{background:linear-gradient(135deg,#f0d9b8,#c49b6c 55%,#6b4a31)}
.ph-c{background:linear-gradient(135deg,#a8433d,#d2b7a4 50%,#4a3b3a)}
.ph-d{background:linear-gradient(135deg,#c7c9c2,#8a7f6e 55%,#3e3a34)}
.ph-e{background:linear-gradient(180deg,#7d96b5,#c5d0da 60%,#3d4652)}
</style>
</head>
<body>
<div class="stage">
  <div class="page">
    <aside class="sidebar">
      <div class="brand"><span class="brand-mark"></span><span class="brand-name">LIFT YOUR BAND</span></div>
      <h1 class="headline">Are you a Producer?<br>Are you an Artist?</h1>
      <div class="like-row"><span class="like-btn">Like</span><span class="like-dot"></span><span>26,491 people like this.</span></div>
      <div class="intro">
        <p>Lorem ipsum dolor sit amet, consectetur adipisic-ing elit, sed do eiusmod tempor incididunt ut labore et dolore magna aliqua. Ut enim ad minim veniam, quis nostrud exercitation ullamco laboris nisi ut aliquip ex ea commodo consequat.</p>
        <p>Duis aute irure dolor in reprehenderit in voluptate velit esse cillum dolore eu fugiat nulla pariatur. Ut enim ad minim veniam, quis nostrud exercitation ullamco laboris nisi ut aliquip ex ea commodo consequat.</p>
      </div>
      <div class="buy-votes">Buy a pack of a dozen votes</div>
      <div class="member-box">
        <div class="signup-btn">Sign Up Now</div>
        <div class="signin-label">Already a Member? Sign In:</div>
        <div class="field email">E-mail</div>
        <div class="field password">Password</div>
        <div class="ok-btn">OK</div>
        <a class="forgot">Forgot Password?</a>
        <div class="connect-btn"><span class="sq"></span>Connect</div>
      </div>
      <div class="follow">
        <span class="follow-label">Follow Us:</span>
        <div class="follow-group">
          <a><span class="dot"></span>FaceSpace</a>
          <a><span class="dot"></span>Chirper</a>
        </div>
      </div>
      <div class="promo" role="img" aria-label="Single artwork: glowing teal and green light rays with dark stars">
        <div class="promo-band">NOVAHILL</div>
        <div class="promo-title">‘Light Up The Sky’</div>
        <div class="promo-sub">Single out now</div>
        <div class="promo-cta">Click for TuneShop</div>
      </div>
      <div class="copyright">© 2011 LiftYourBand.net. All rights reserved.</div>
    </aside>

    <section class="main">
      <header class="main-head">
        <h2 class="main-title">Top Artists</h2>
        <nav class="pager"><span class="label">Showing:</span><a class="current">1-10</a><a>11-20</a><a>21-30</a><a>41-50</a><a>51-60</a><a>61-70</a><a>71-80</a><a>81-90</a><a>91-100</a></nav>
      </header>
      <ol class="artist-list">
        <li class="artist"><span class="rank">1</span><div class="photo ph-a" role="img" aria-label="Photo of Evan Marlowe"></div><span class="name">Evan Marlowe</span><span class="link">fansbackrecords.co.uk/Artists/evanmarlowemusic/</span><span class="votes up">1225</span><span class="vote-btn">Vote</span><span class="funds">£ 18,280 / £ 100,000</span></li>
        <li class="artist"><span class="rank">2</span><div class="photo ph-b" role="img" aria-label="Photo of Weavers Son"></div><span class="name">Weavers Son</span><span class="link">fansbackrecords.co.uk/Artists/weaversson/</span><span class="votes up">1201</span><span class="vote-btn">Vote</span><span class="funds">£ 2,880 / £ 100,000</span></li>
        <li class="artist"><span class="rank">3</span><div class="photo ph-c" role="img" aria-label="Photo of The Brightwells"></div><span class="name">The Brightwells</span><span class="link">fansbackrecords.co.uk/Artists/thebrightwells/</span><span class="votes up">1195</span><span class="vote-btn">Vote</span><span class="funds">£ 18,870 / £ 100,000</span></li>
        <li class="artist"><span class="rank">4</span><div class="photo ph-d" role="img" aria-label="Photo of Ramparts"></div><span class="name">Ramparts</span><span class="link">fansbackrecords.co.uk/Artists/ramparts/</span><span class="votes down">1120</span><span class="vote-btn">Vote</span><span class="funds">£ 3,330 / £ 100,000</span></li>
        <li class="artist"><span class="rank">5</span><div class="photo ph-e" role="img" aria-label="Photo of Tiles"></div><span class="name">Tiles</span><span class="link">fansbackrecords.co.uk/Artists/tiles/</span><span class="votes down">1102</span><span class="vote-btn">Vote</span><span class="funds">£ 3,160 / £ 100,000</span></li>
        <li class="artist"><span class="rank">6</span><div class="photo ph-a" role="img" aria-label="Photo of Evan Marlowe"></div><span class="name">Evan Marlowe</span><span class="link">fansbackrecords.co.uk/Artists/evanmarlowemusic/</span><span class="votes up">1099</span><span class="vote-btn">Vote</span><span class="funds">£ 18,280 / £ 100,000</span></li>
        <li class="artist"><span class="rank">7</span><div class="photo ph-b" role="img" aria-label="Photo of Weavers Son"></div><span class="name">Weavers Son</span><span class="link">fansbackrecords.co.uk/Artists/weaversson/</span><span class="votes down">1078</span><span class="vote-btn">Vote</span><span class="funds">£ 2,880 / £ 100,000</span></li>
        <li class="artist"><span class="rank">8</span><div class="photo ph-c" role="img" aria-label="Photo of The Brightwells"></div><span class="name">The Brightwells</span><span class="link">fansbackrecords.co.uk/Artists/thebrightwells/</span><span class="votes up">985</span><span class="vote-btn">Vote</span><span class="funds">£ 18,870 / £ 100,000</span></li>
        <li class="artist"><span class="rank">9</span><div class="photo ph-d" role="img" aria-label="Photo of Ramparts"></div><span class="name">Ramparts</span><span class="link">fansbackrecords.co.uk/Artists/ramparts/</span><span class="votes down">785</span><span class="vote-btn">Vote</span><span class="funds">£ 3,160 / £ 100,000</span></li>
        <li class="artist"><span class="rank">10</span><div class="photo ph-e" role="img" aria-label="Photo of Tiles"></div><span class="name">Tiles</span><span class="link">fansbackrecords.co.uk/Artists/tiles/</span><span class="votes down">236</span><span class="vote-btn">Vote</span><span class="funds">£ 3,160 / £ 100,000</span></li>
      </ol>
      <footer class="main-foot">
        <nav class="pager"><span class="label">Showing:</span><a class="current">1-10</a><a>11-20</a><a>21-30</a><a>41-50</a><a>51-60</a><a>61-70</a><a>71-80</a><a>81-90</a><a>91-100</a></nav>
      </footer>
    </section>
  </div>
</div>
</body>
</html>
```